New Business Card for Innovative Tool Company

We need a new design of business card for our florida based tool manufacturing company. I will attach 2 files that we use for our logo, use whichever you feel works best for the card. Main colours are as per logo, and we can use different shades of black/white/grey for the background.

Contact Information for Business Card

Name/Jobtitle/cell
Corvalen Tools
Suite 212c
4316 Marrowdale Pkw
Orlando, FL32847
USA
name@corvaleninc.example
www.corvaleninc.example

Font styles to use
Sans Serif

Colors

Designer to choose colors to be used in the design.

Requirements
Must have
• Icons for Plazaro, Chirpet, Snapvale, Findlo & Vidstream

```html
<!DOCTYPE html>
<html lang="en">
<head>
<meta charset="utf-8">
<title>Corvalen Tools – Business Card</title>
<link href="https://fonts.googleapis.com/css2?family=Roboto:wght@400;500;700&family=Roboto+Condensed:wght@700&display=swap" rel="stylesheet">
<style>
  :root {
    --backdrop: #8a8a8a;
    --card: #353535;
    --card-deep: #2a2a2a;
    --emboss: #262626;
    --emboss-light: #4a4a4a;
    --text-light: #d9d9d9;
    --accent: #f2ea2c;
  }
  * { margin: 0; padding: 0; box-sizing: border-box; }
  html, body { width: 1200px; height: 900px; overflow: hidden; }
  body {
    background: var(--backdrop);
    font-family: "Roboto", Arial, sans-serif;
    display: flex;
    flex-direction: column;
    align-items: center;
    justify-content: center;
    gap: 40px;
  }
  .card {
    position: relative;
    width: 700px;
    height: 400px;
    background: var(--card);
    border-bottom: 6px solid var(--accent);
    box-shadow: 0 10px 24px rgba(0,0,0,.35);
  }
  .card--back { border-left: 6px solid var(--accent); }

  .identity {
    position: absolute;
    left: 150px;
    top: 150px;
    text-align: right;
  }
  .identity__name {
    font-family: "Roboto Condensed", Arial, sans-serif;
    font-weight: 700;
    font-size: 30px;
    letter-spacing: 2px;
    color: var(--emboss);
    text-shadow: 0 1px 0 var(--emboss-light);
    text-transform: uppercase;
  }
  .identity__role {
    font-size: 15px;
    color: var(--emboss);
    text-shadow: 0 1px 0 var(--emboss-light);
  }
  .divider {
    position: absolute;
    left: 400px;
    top: 130px;
    width: 2px;
    height: 76px;
    background: var(--emboss-light);
  }
  .contacts {
    position: absolute;
    left: 425px;
    top: 130px;
    list-style: none;
    font-size: 16px;
    color: var(--text-light);
    line-height: 26px;
  }
  .contacts li { display: flex; align-items: center; gap: 10px; }
  .contacts svg { width: 12px; height: 12px; fill: none; stroke: var(--text-light); stroke-width: 1.4; }
  .address {
    position: absolute;
    left: 0; right: 0;
    bottom: 36px;
    text-align: center;
    font-size: 16px;
    letter-spacing: .5px;
    color: var(--emboss);
    text-shadow: 0 1px 0 var(--emboss-light);
  }

  .brand {
    position: absolute;
    inset: 0;
    display: flex;
    align-items: center;
    justify-content: center;
    gap: 16px;
  }
  .brand__mark {
    width: 40px; height: 40px;
    border: 2px solid #9a9a9a;
    border-radius: 50%;
  }
  .brand__name {
    font-size: 44px;
    font-weight: 700;
    letter-spacing: 3px;
    color: #b5b5b5;
    text-transform: uppercase;
  }
</style>
</head>
<body>
  <section class="card card--back" aria-label="Card back">
    <div class="identity">
      <p class="identity__name">Dorian Kessler</p>
      <p class="identity__role">Director</p>
    </div>
    <span class="divider"></span>
    <ul class="contacts">
      <li>
        <svg viewBox="0 0 12 12"><path d="M2 1.5h2.2l1 2.5-1.4 1a6 6 0 0 0 3.2 3.2l1-1.4 2.5 1V10a1 1 0 0 1-1 1A9 9 0 0 1 1 2.5a1 1 0 0 1 1-1z"/></svg>
        +330 5813-4072
      </li>
      <li>
        <svg viewBox="0 0 12 12"><rect x="1" y="2.5" width="10" height="7"/><path d="M1 2.5l5 4 5-4"/></svg>
        name@corvaleninc.example
      </li>
      <li>
        <svg viewBox="0 0 12 12"><circle cx="6" cy="6" r="5"/><path d="M1 6h10M6 1c-2.5 3-2.5 7 0 10M6 1c2.5 3 2.5 7 0 10"/></svg>
        www.corvaleninc.example
      </li>
    </ul>
    <p class="address">Suite 212c 4316 Marrowdale Pkw Orlando, FL32847 USA</p>
  </section>

  <section class="card card--front" aria-label="Card front">
    <div class="brand">
      <span class="brand__mark"></span>
      <span class="brand__name">Corvalen Tools</span>
    </div>
  </section>
</body>
</html>
```